Android app Promotional Graphics

I need 2 sizes of promotional graphics for my existing Android app that already has an icon, website, etc. The app is an aggregator of Daily Deals from sites such as zibba.com, morvo.com, flintcart.com.

You can see the existing icon etc here:
http://findbargainnest.com

You can also download high resolution versions from here: http://findbargainnest.com/press

The 2 sizes I need are:
Promo Graphic:
180w x 120h
24 bit PNG or JPEG (no alpha)
No border in art

Feature Graphic:
1024 x 500
Will be downsized to mini or micro

Google has specific guidelines for the Feature Graphic here:
http://appmakers-notes.examplehost.com/2011/10/app-shelf-featured-image.html

This page has guidelines for all the graphics including the 2 I need (3rd and 4th bullet points):
https://help.plinthware.com/appshelf/publisher/support/bin/answer.py?hl=en&answer=5531906

I do NOT want the promotional graphics to include screenshots as they change too often. For any text please use what you think is appropriate from findbargainnest.com. It should at least have the app name "Bargain Nest".

Edit: Added some additional text.
It would also be good to have the phrase "Daily Deals" or "1,000's of Daily Deals in 1 place" if there is room.

Industry/Entity Type

Android

Logo Text

Bargain Nest

Requirements
Must have
• Must meet Google's specifications for size, etc and must also follow the guidelines. All of which I included links to in the description.
Should not have
• Screenshots.

```html
<!DOCTYPE html>
<html lang="en">
<head>
<meta charset="utf-8">
<title>Bargain Nest – Promotional Graphics</title>
<link rel="stylesheet" href="https://fonts.googleapis.com/css2?family=Archivo+Black&family=Nunito+Sans:wght@600;700&family=Open+Sans:wght@400;600;700&display=swap">
<style>
  :root{
    --board:#c6c6c6;
    --ink:#0a0a0a;
    --green-light:#2fb82e;
    --green:#24a024;
    --green-dark:#1c821c;
    --tile:#1f7c1f;
    --tile-edge:#16601a;
    --brand-text:#cfdccf;
    --phone-black:#000;
    --bar:#3a3a3a;
    --grid-gray:#7d7d7d;
    --grid-line:#5f5f5f;
    --white:#fff;
    --muted:#e0e0e0;
    --star:#e8e8e8;
    --star-off:#9a9a9a;
    --cyan:#1fe6f2;
  }
  *{box-sizing:border-box;margin:0;padding:0}
  html,body{width:1200px;height:900px;overflow:hidden}
  body{background:var(--board);position:relative;font-family:"Nunito Sans",Arial,sans-serif}
  .size-label{position:absolute;font-family:"Archivo Black",Arial,sans-serif;font-size:22px;color:var(--ink);text-align:center;width:200px}

  .promo{position:absolute;overflow:hidden;background:linear-gradient(135deg,var(--green-light),var(--green) 45%,var(--green-dark))}
  .promo .deco{position:absolute;border-radius:28%;background:rgba(0,0,0,.07)}
  .app-tile{position:absolute;border-radius:22%;background:linear-gradient(var(--tile),var(--tile-edge));box-shadow:0 2px 6px rgba(0,0,0,.35)}
  .brand-name,.tagline{position:absolute;color:var(--brand-text);font-weight:700;white-space:nowrap;line-height:1}
  .tagline{font-weight:600}

  /* feature graphic */
  .feature{left:385px;top:243px;width:753px;height:368px}
  .feature .app-tile{left:68px;top:82px;width:200px;height:200px;border-radius:36px}
  .feature .brand-name{left:298px;top:120px;font-size:72px}
  .feature .tagline{left:340px;top:204px;font-size:52px}

  /* small promo */
  .mini{left:146px;top:183px;width:180px;height:120px}
  .mini .app-tile{left:65px;top:14px;width:48px;height:48px;border-radius:10px}
  .mini .brand-name{left:0;width:180px;text-align:center;top:72px;font-size:21px}
  .mini .tagline{left:0;width:180px;text-align:center;top:93px;font-size:14px}

  /* phone preview */
  .phone{position:absolute;left:116px;top:377px;width:240px;height:400px;background:var(--phone-black);overflow:hidden;font-family:"Open Sans",Arial,sans-serif}
  .status-bar{position:absolute;left:0;top:0;width:240px;height:18px;color:var(--white);font-size:10px;font-weight:700}
  .status-bar svg{position:absolute;left:118px;top:3px}
  .status-bar .clock{position:absolute;right:6px;top:2px}
  .action-bar{position:absolute;left:0;top:18px;width:240px;height:32px;background:repeating-linear-gradient(135deg,#333 0 2px,#3c3c3c 2px 4px)}
  .action-bar .shelf-mark{position:absolute;left:18px;top:8px;width:18px;height:16px;background:#d6d6d6;border-radius:2px}
  .action-bar .title{position:absolute;left:47px;top:5px;color:var(--white);font-size:17px}
  .action-bar svg{position:absolute;right:6px;top:6px}
  .phone .banner{left:0;top:50px;width:240px;height:118px}
  .banner .app-tile{left:22px;top:26px;width:64px;height:64px;border-radius:13px}
  .banner .brand-name{left:94px;top:38px;font-size:20px}
  .banner .tagline{left:110px;top:62px;font-size:16px}

  .categories{position:absolute;left:0;top:170px;width:118px;height:176px}
  .category{position:relative;height:44px;background:var(--grid-gray);border-bottom:1px solid var(--grid-line);color:var(--white)}
  .category::before{content:"";position:absolute;left:0;top:0;width:24px;height:100%;background:var(--accent);opacity:.55}
  .category .name{position:absolute;left:10px;top:2px;font-size:14px;font-weight:700}
  .category .more{position:absolute;right:6px;bottom:4px;font-size:9px;color:var(--muted)}
  .apps{--accent:#b5c22c}.games{--accent:#c7c22e}.books{--accent:#3a8fd8}.movies{--accent:#d23a3a}

  .promo-tile{position:absolute;left:0;top:350px;width:118px;height:50px;background:var(--cyan)}

  .listing{position:absolute;left:122px;width:118px}
  .phone .featured{top:170px;height:56px}
  .featured .app-tile{left:14px;top:13px;width:28px;height:28px;border-radius:6px}
  .featured .brand-name{left:46px;top:17px;font-size:11px}
  .featured .tagline{left:52px;top:31px;font-size:8px}
  .item{height:56px;background:var(--grid-gray);color:var(--white)}
  .item .cover{position:absolute;left:6px;top:6px;width:24px;height:32px}
  .item .title{position:absolute;left:38px;top:4px;font-size:10px;font-weight:700;line-height:12px;width:78px}
  .item .author{position:absolute;left:38px;top:30px;font-size:9px;color:var(--muted)}
  .item .stars{position:absolute;left:6px;bottom:2px;font-size:10px;color:var(--star);letter-spacing:-1px}
  .item .stars span{color:var(--star-off)}
  .item .price{position:absolute;right:3px;bottom:3px;font-size:9px;color:var(--muted)}
</style>
</head>
<body>

  <div class="size-label" style="left:136px;top:135px">180x120</div>
  <div class="size-label" style="left:646px;top:199px">1024x500</div>
  <div class="size-label" style="left:134px;top:343px">PREVIEW</div>

  <div class="promo mini">
    <div class="deco" style="left:120px;top:-10px;width:90px;height:80px"></div>
    <div class="deco" style="left:-30px;top:60px;width:70px;height:80px"></div>
    <div class="app-tile"></div>
    <div class="brand-name">Bargain Nest</div>
    <div class="tagline">Daily Deals</div>
  </div>

  <div class="promo feature">
    <div class="deco" style="left:335px;top:-40px;width:330px;height:350px"></div>
    <div class="deco" style="left:425px;top:-60px;width:400px;height:160px"></div>
    <div class="deco" style="left:525px;top:40px;width:300px;height:380px"></div>
    <div class="deco" style="left:-60px;top:220px;width:300px;height:220px"></div>
    <div class="app-tile"></div>
    <div class="brand-name">Bargain Nest</div>
    <div class="tagline">Daily Deals</div>
  </div>

  <div class="phone">
    <div class="status-bar">
      <svg width="76" height="12" viewBox="0 0 76 12" aria-hidden="true">
        <path d="M2 3l5 5-2.5 2V1L7 3 2 8" fill="none" stroke="#ccc" stroke-width="1"/>
        <path d="M14 6a8 8 0 0 1 12 0M17 8a4 4 0 0 1 6 0" fill="none" stroke="#8bd13c" stroke-width="1.6"/>
        <circle cx="20" cy="10" r="1.2" fill="#8bd13c"/>
        <rect x="32" y="3" width="3" height="8" fill="#8bd13c"/><rect x="36" y="3" width="3" height="8" fill="#8bd13c"/>
        <rect x="46" y="8" width="2" height="3" fill="#8bd13c"/><rect x="49" y="6" width="2" height="5" fill="#8bd13c"/>
        <rect x="52" y="4" width="2" height="7" fill="#8bd13c"/><rect x="55" y="2" width="2" height="9" fill="#8bd13c"/>
        <rect x="63" y="1" width="7" height="11" fill="#ddd"/><rect x="64" y="4" width="5" height="7" fill="#8bd13c"/>
      </svg>
      <span class="clock">2:28</span>
    </div>
    <div class="action-bar">
      <div class="shelf-mark"></div>
      <div class="title">App Shelf</div>
      <svg width="20" height="20" viewBox="0 0 20 20" aria-hidden="true">
        <circle cx="8" cy="8" r="6" fill="none" stroke="#fff" stroke-width="2"/>
        <path d="M12.5 12.5l6 6" stroke="#fff" stroke-width="2.5" stroke-linecap="round"/>
      </svg>
    </div>

    <div class="promo banner">
      <div class="deco" style="left:130px;top:-20px;width:140px;height:100px"></div>
      <div class="app-tile"></div>
      <div class="brand-name">Bargain Nest</div>
      <div class="tagline">Daily Deals</div>
    </div>

    <div class="categories">
      <div class="category apps"><span class="name">Apps</span><span class="more">see more ›</span></div>
      <div class="category games"><span class="name">Games</span><span class="more">see more ›</span></div>
      <div class="category books"><span class="name">Books</span><span class="more">see more ›</span></div>
      <div class="category movies"><span class="name">Movies</span><span class="more">see more ›</span></div>
    </div>

    <div class="promo-tile" role="img" aria-label="Promo tile for a game with a cartoon sea creature on a cyan background"></div>

    <div class="promo listing featured">
      <div class="app-tile"></div>
      <div class="brand-name">Bargain Nest</div>
      <div class="tagline">Daily Deals</div>
    </div>

    <div class="listing item" style="top:230px">
      <div class="cover" role="img" aria-label="Book cover" style="background:linear-gradient(#fff,#f2c6e6)"></div>
      <div class="title">The Pegasus Whisperer</div>
      <div class="author">Missy Bloom</div>
      <div class="stars">★★<span>★★★</span></div>
      <div class="price">$13.99</div>
    </div>
    <div class="listing item" style="top:290px">
      <div class="cover" role="img" aria-label="Book cover" style="background:linear-gradient(#e23a2e,#f4f4f4)"></div>
      <div class="title">Dancing with Pandas</div>
      <div class="author">George Chiu</div>
      <div class="stars">★★★<span>★★</span></div>
      <div class="price">$2.99</div>
    </div>
    <div class="listing item" style="top:350px">
      <div class="cover" role="img" aria-label="Book cover" style="background:linear-gradient(#222,#4a3a20)"></div>
      <div class="title">Rebecca's Tangled Web</div>
      <div class="author">Seymour Huff</div>
      <div class="stars">★★★<span>★★</span></div>
      <div class="price">$0.99</div>
    </div>
  </div>

</body>
</html>
```